Redesign two student school awards

I need to redesign 2 students awards. I need the elements of the letterhead to be incorporated into the Student Awards. I have covered some of the letterhead elements to show just the 4 elements that need to be incorporated: school emblem, school name, "Steadfast in service, bold in learning.", and the 3 coloured ribbon. The awards need to be in colour and the use of the 3 school colours - purple, yellow (gold) and chocolate brown,

I have upload the 2 awards the school presents to students (they are printed on A4 Paper). The first one is the:

(1) Year Adviser Award - this award needs to include the school name; the title: Year Adviser's Award; Award to; Name (where the word is deleted and the office staff type the students name or uploaded names which can be autofilled); for the following achievements; the year (which can be changed an include the day and month (but auto filled); Year Adviser (where the teacher signs their name - see lower left of the award; (also the 5 categories - School Service, Community Service , Sporting Achievements, Leadership, Academic Achievement (these 5 categories must be able to be deleted as a student may receive the Year Adviser's Award for 1 or 2 of the categories)

(2) Principal's Award - all elements of this award need to be included. In this example there's a fake name Dale Foster - this is where the office staff type in the students name or hopefully upload a list of names that are auto filled. The 5 categories need to be retained e.g. School Service, Community Service etc (these can be fixed as they are not deleted; for the following achievements; the year (which can be changed an include the day and month (but auto filled); my name and title,

For the 2 student awards it would be good if the design is in a computer program where the office staff can auto fill students names.

The main goal is to redesign the 2 awards, whilst retaining current elements and include 4 of the elements from the letter head.

Target Market(s)

School students (12 years old to 18 years old)

Industry/Entity Type

Education

Font styles to use
Serif

Requirements
Must have
• The elements and school colours mentioned in the description. Would be helpful if the computer program it is contained in allows for auto fill of student names, date, and for the Year Advisers award any one of the five award categories can be removed. To be printed on A4 paper/card

Colours must contain the school colours as mentioned before and the 4 elements of the letterhead. I am trying to have all our communications and awards contain similar elements.

```html
<!DOCTYPE html>
<html lang="en">
<head>
<meta charset="utf-8">
<title>Year Adviser's Award – Kell River Memorial High School</title>
<link href="https://fonts.googleapis.com/css2?family=Oswald:wght@300;400&family=Kaushan+Script&display=swap" rel="stylesheet">
<style>
  :root {
    --backdrop: #e9e8e4;
    --sheet: #ecebe6;
    --panel: #f4f3ef;
    --purple: #7a2f86;
    --gold: #e6dc1e;
    --brown: #3a2418;
    --olive: #8f8d22;
    --ink: #2b2b2b;
    --grey: #555555;
  }
  * { margin: 0; padding: 0; box-sizing: border-box; }
  html, body { width: 1200px; height: 866px; overflow: hidden; }
  body { background: var(--backdrop); font-family: "Oswald", sans-serif; color: var(--ink); }

  .certificate {
    position: absolute; left: 317px; top: 33px;
    width: 566px; height: 800px;
    background: var(--sheet);
    box-shadow: 0 2px 10px rgba(0,0,0,.12);
  }
  .certificate__pattern {
    position: absolute; inset: 0;
    background: linear-gradient(180deg, #eeeee9, #e6e5e0);
  }
  .certificate__frame { position: absolute; inset: 0; }
  .certificate > .block {
    position: absolute; left: 0; width: 566px;
    text-align: center; line-height: 1; font-weight: 400;
  }

  .school-mark { top: 112px; display: flex; justify-content: center; align-items: center; gap: 8px; }
  .school-mark__dot { width: 14px; height: 14px; border-radius: 50%; background: var(--purple); }
  .school-mark__name { font-size: 18px; color: var(--purple); letter-spacing: 1px; }

  .school-name { top: 180px; font-size: 20px; letter-spacing: .5px; color: #111111; }
  .school-motto { top: 205px; font-size: 10px; font-weight: 300; color: var(--grey); }
  .award-title { top: 236px; font-size: 26px; color: var(--purple); }

  .cert-heading { top: 326px; font-family: "Kaushan Script", cursive; font-size: 32px; color: var(--olive); }
  .cert-sub { top: 362px; font-size: 9px; letter-spacing: 1px; color: var(--grey); }

  .awarded-label { top: 418px; font-size: 16px; font-weight: 300; letter-spacing: 1px; }
  .recipient { top: 446px; font-size: 36px; letter-spacing: 2px; color: #222222; }
  .recipient__rule { position: absolute; top: 490px; left: 184px; width: 198px; height: 3px; background: var(--ink); }

  .achievements-label { top: 545px; font-size: 14px; font-weight: 300; color: var(--olive); letter-spacing: .5px; }
  .achievement { top: 575px; font-size: 23px; letter-spacing: 1px; }

  .sign-off { position: absolute; top: 666px; font-size: 12px; line-height: 1.2; text-align: center; color: var(--grey); }
  .sign-off--principal { left: 150px; width: 130px; }
  .sign-off__name { font-size: 11px; font-weight: 300; margin-top: 4px; }
  .sign-off__signature {
    width: 110px; height: 30px; margin: 8px auto 0; border-radius: 4px;
    background: linear-gradient(90deg, rgba(30,30,30,.15), rgba(30,30,30,.35), rgba(30,30,30,.15));
  }
  .sign-off--year { left: 325px; width: 80px; }
  .sign-off__seal { width: 40px; height: 40px; border-radius: 50%; margin: 6px auto 0; background: #dfe0ee; border: 2px solid #5663a8; }
</style>
</head>
<body>
  <main class="certificate">
    <div class="certificate__pattern" role="img" aria-label="Faint grey hexagon background pattern"></div>

    <svg class="certificate__frame" width="566" height="800" viewBox="0 0 566 800">
      <polygon points="40,22 540,28 522,774 18,780" fill="var(--brown)"/>
      <polygon points="44,26 536,32 518,770 22,776" fill="var(--purple)"/>
      <polygon points="58,32 522,40 505,760 36,766" fill="var(--gold)"/>
      <polygon points="62,36 518,44 502,756 40,762" fill="var(--panel)"/>
      <line x1="52" y1="271" x2="423" y2="271" stroke="var(--purple)" stroke-width="3"/>
      <circle cx="423" cy="271" r="3.5" fill="var(--purple)"/>
      <line x1="138" y1="643" x2="507" y2="643" stroke="var(--purple)" stroke-width="3"/>
      <circle cx="138" cy="643" r="3.5" fill="var(--purple)"/>
    </svg>

    <div class="block school-mark">
      <span class="school-mark__dot"></span>
      <span class="school-mark__name">KELL RIVER</span>
    </div>
    <h1 class="block school-name">KELL RIVER MEMORIAL HIGH SCHOOL</h1>
    <p class="block school-motto">“Steadfast in service, bold in learning.”</p>
    <h2 class="block award-title">YEAR ADVISER’S AWARD</h2>

    <p class="block cert-heading">Certificate</p>
    <p class="block cert-sub">OF ACHIEVEMENTS</p>

    <p class="block awarded-label">AWARDED TO</p>
    <p class="block recipient">DALE FOSTER</p>
    <span class="recipient__rule"></span>

    <p class="block achievements-label">FOR THE FOLLOWING ACHIEVEMENTS:</p>
    <p class="block achievement">«SPORTING ACHIEVEMENT»</p>

    <div class="sign-off sign-off--principal">
      <p>Principal:</p>
      <p class="sign-off__name">Mr J. Whitlock</p>
      <div class="sign-off__signature" role="img" aria-label="Principal's handwritten signature"></div>
    </div>
    <div class="sign-off sign-off--year">
      <p>Year:</p>
      <div class="sign-off__seal"></div>
    </div>
  </main>
</body>
</html>
```